BRIGHTDESK - Remote Tech Support Site

We are looking for a new very responsive and simple website for our brand Brightdesk.com - a remote technical support company.

This company supports customers Globally in different countries throughout Eur/ North America / South America / Asia etc (please keep this in mind and integrate into the idea).

Its important to us that the design is very explanatory, the customer should easily be able to figure out that we provide computer support right away ... I like one page responsive type designs as well without a bunch of menu items

Here are some similar sites we like - but still looking for a unique design that fits out brand "brightdesk" - I have upload also some layouts i like (but the designs are not important just the layouts), youll see it includes consumer business etc which is important.

VOLM.COM - I love how clean it is - nice and white easy to see everything

PLUMWIRE247.COM - also nice the layout and responsive one page design makes it easy to use

corvalfix.com - similar to plumwire design as well - you can get the idea im looking for between the two

You will notice those examples are much different then the attachments I added - again this is more of an idea for possible layouts .. attached is also the logo - could inspire color scheme / blue white black etc

Target Market(s)

Home consumers without computer knowledge , older age 45-65, small medium business ... computer repair - slow computers

Industry/Entity Type

Computer Repair

Logo Text

Brightdesk

Coding

Coded - Design and coding required

Number of Pages Required

1 page

Font styles to use
Sans Serif
Other font styles liked:
• your choice responsive

Colors

Designer to choose colors to be used in the design.

Requirements
Must have
• Clean - responsive - professional design - the name says it all - brightdesk
• CALL TO ACTIONS FOR "Get Help Now!" / "Learn More" etc
Nice to have
• We are looking for a new very responsive and simple website for our brand Brightdesk.com - a remote technical support company.
• This company supports customers Globally in different countries throughout Eur/ North America / South America / Asia etc (please keep this in mind and integrate into the idea).
• Its important to us that the design is very explanatory, the customer should easily be able to figure out that we provide computer support right away ... I like one page responsive type designs as well without a bunch of menu items
• Here are some similar sites we like - but still looking for a unique design that fits out brand "brightdesk" - I have upload also some layouts i like (but the designs are not important just the layouts), youll see it includes consumer business etc which is important.
• VOLM.COM - I love how clean it is - nice and white easy to see everything
• PLUMWIRE247.COM - also nice the layout and responsive one page design makes it easy to use
• corvalfix.com - similar to plumwire design as well - you can get the idea im looking for between the two
Should not have
• dark, packed page - bad small font -

```html
<!DOCTYPE html>
<html lang="en">
<head>
<meta charset="utf-8">
<title>Brightdesk – Remote Tech Support</title>
<link href="https://fonts.googleapis.com/css2?family=Montserrat:wght@400;500;600;700&family=Open+Sans:wght@400;600&family=Poppins:wght@400;500;600&family=Raleway:wght@600;700&display=swap" rel="stylesheet">
<style>
:root{
  --blue:#1e8fff;
  --sky:#12a6ee;
  --ink:#222;
  --text:#666;
  --card:#f4f4f4;
  --plan-bg:#f6f8fb;
  --footer:#1c1c1c;
  --white:#fff;
}
*{box-sizing:border-box;margin:0;padding:0}
html,body{width:1200px;height:3249px;overflow:hidden}
body{position:relative;font-family:"Open Sans",sans-serif;color:var(--text);background:var(--white)}
section,header,footer{position:absolute;left:0;width:1200px}

/* hero */
.hero{top:0;height:624px;overflow:hidden}
.hero-photo{position:absolute;inset:0;background:linear-gradient(135deg,#5d6670 0%,#8b939b 40%,#6f7780 70%,#4d555d 100%)}
.hero-shade{position:absolute;inset:0;background:rgba(30,35,45,.35)}
.topbar{position:absolute;top:0;left:0;width:1200px;height:40px;background:rgba(20,22,28,.55);font-size:14px;color:var(--white)}
.topbar span{position:absolute;top:10px}
.login{position:absolute;left:1057px;top:6px;width:67px;height:28px;background:var(--sky);color:#fff;font-family:Montserrat,sans-serif;font-size:12px;font-weight:500;text-align:center;line-height:28px}
.brand{position:absolute;left:87px;top:58px;display:flex;align-items:center;gap:10px;font-family:Montserrat,sans-serif;font-weight:600;font-size:30px;color:#fff}
.brand i{width:40px;height:40px;border-radius:50%;background:var(--blue);display:block}
.nav a{position:absolute;top:74px;font-family:Montserrat,sans-serif;font-size:14px;color:#fff;text-decoration:none}
.nav .active:after{content:"";position:absolute;left:0;right:0;top:36px;height:3px;background:var(--blue)}
.hero h1{position:absolute;top:258px;width:1200px;text-align:center;font-family:Raleway,sans-serif;font-weight:700;font-size:52px;color:#fff;letter-spacing:1px}
.hero h2{position:absolute;top:318px;width:1200px;text-align:center;font-family:Raleway,sans-serif;font-weight:700;font-size:48px;color:var(--blue)}
.btn{position:absolute;height:52px;border-radius:26px;font-family:Montserrat,sans-serif;font-weight:600;font-size:16px;text-align:center;line-height:52px}
.btn-white{left:454px;top:396px;width:160px;background:#fff;color:#222}
.btn-blue{left:628px;top:396px;width:160px;background:var(--sky);color:#fff}
.arrow{position:absolute;top:312px}
.dots{position:absolute;top:555px;left:512px;display:flex;gap:6px}
.dots i{width:12px;height:12px;border-radius:50%;background:#fff;display:block}
.dots i.on{background:transparent;border:2px solid #fff;width:16px;height:16px;margin-top:-2px}

/* features */
.features{top:624px;height:351px}
.fcard{position:absolute;top:106px;width:225px;height:227px;background:var(--card);text-align:center}
.fcard .ico{position:absolute;left:70px;top:-43px;width:86px;height:86px;border-radius:50%;display:flex;align-items:center;justify-content:center}
.fcard h3{margin-top:78px;font-family:Montserrat,sans-serif;font-weight:500;font-size:14px;color:#444}
.fcard p{margin:18px auto 0;width:170px;font-size:13px;line-height:22px;color:#777}

/* blue band */
.band{top:1035px;height:481px;background:var(--blue);color:#fff;overflow:hidden}
.band-rule{position:absolute;left:0;top:193px;width:1200px;height:1px;background:rgba(255,255,255,.55)}
.band-deco{position:absolute;left:975px;top:95px;width:210px;height:330px;border:2px solid rgba(255,255,255,.1);border-radius:26px}
.band-box{position:absolute;left:87px;top:63px;width:251px;height:345px;border:1px solid rgba(255,255,255,.8)}
.svc{position:absolute;top:115px;width:251px;text-align:center}
.svc svg{display:block;margin:0 auto}
.svc h3{margin-top:48px;font-family:Montserrat,sans-serif;font-weight:700;font-size:15px}
.svc p{margin:16px auto 0;width:220px;font-size:11.5px;line-height:23px}
.svc a{display:block;margin-top:16px;font-family:Montserrat,sans-serif;font-size:11px;font-weight:700;color:#fff;text-decoration:none}

/* services */
.range{top:1516px;height:535px}
.range h2{position:absolute;left:108px;top:76px;font-family:Montserrat,sans-serif;font-weight:700;font-size:26px;line-height:38px;color:#222}
.range .lead{position:absolute;left:108px;top:172px;width:440px;font-size:13px;line-height:23px;color:#aaa}
.item{position:absolute;font-size:13px;color:#555;display:flex;align-items:center;gap:22px;white-space:nowrap}
.sq{position:absolute;top:409px;height:39px;font-family:Montserrat,sans-serif;font-weight:600;font-size:11px;text-align:center;line-height:37px}
.sq.fill{left:108px;width:162px;background:var(--blue);color:#fff;line-height:39px}
.sq.line{left:290px;width:124px;border:1px solid #333;color:#222}
.device-art{position:absolute;left:693px;top:87px;width:336px;height:400px;border-radius:30px;background:linear-gradient(160deg,#3a3d44 0%,#6b7078 45%,#2a2c31 100%)}
.vdots{position:absolute;left:1094px;top:256px}

/* plans */
.plans{top:2051px;height:511px;background:var(--plan-bg);text-align:center}
.plans h2{margin-top:40px;font-family:Poppins,sans-serif;font-weight:400;font-size:38px;color:#222}
.plans .sub{margin:14px auto 0;width:880px;font-size:15px;line-height:26px;color:#888}
.plan{position:absolute;top:189px;width:218px;height:257px;background:#fff;border:1px solid #e6e9ee}
.plan h4{margin-top:24px;font-family:Montserrat,sans-serif;font-weight:600;font-size:16px;color:#333}
.plan .price{margin-top:6px;font-family:Poppins,sans-serif;font-size:50px;line-height:56px;color:var(--blue)}
.plan .price sup{font-size:24px;vertical-align:22px}
.plan .at{font-size:11px;color:#777}
.plan p{margin:14px auto 0;width:160px;font-size:13px;line-height:21px;color:#777}
.plan .go{display:block;margin:18px auto 0;width:119px;height:37px;background:var(--blue);color:#fff;font-family:Montserrat,sans-serif;font-weight:600;font-size:11px;line-height:37px}

/* regions */
.regions{top:2562px;height:323px;text-align:center}
.regions h2{margin-top:68px;font-family:Montserrat,sans-serif;font-weight:600;font-size:24px;color:#222}
.regions .sub{margin-top:6px;font-size:13px;color:#aaa}
.regions .rule{width:60px;height:3px;background:var(--blue);margin:14px auto 0}
.rname{position:absolute;top:198px;width:180px;margin-left:-90px;font-family:Montserrat,sans-serif;font-weight:700;font-size:21px;color:#b9b9b9;letter-spacing:1px}

/* footer */
.footer{top:2885px;height:364px;background:var(--footer);color:#bbb;font-size:12.5px}
.fcol{position:absolute;top:52px;width:240px}
.fcol h4{font-family:Montserrat,sans-serif;font-weight:600;font-size:15px;color:#fff}
.fcol .rule{width:40px;height:2px;background:var(--blue);margin:12px 0 20px}
.fcol p{line-height:23px}
.fcol li{list-style:none;line-height:24px;display:flex;gap:10px;align-items:flex-start}
.fcol li:before{content:"";width:0;height:0;border-left:5px solid #ccc;border-top:4px solid transparent;border-bottom:4px solid transparent;margin-top:8px}
.fcol .contact li:before{display:none}
.social{display:flex;gap:12px;margin-top:20px}
.social i{width:36px;height:36px;border-radius:50%;background:#333;display:block}
.copy{position:absolute;top:323px;width:1200px;text-align:center;font-size:12px;color:#aaa}
</style>
</head>
<body>

<header class="hero">
  <div class="hero-photo" role="img" aria-label="Overhead photo of a work desk with a laptop, glasses, coffee cup and plant"></div>
  <div class="hero-shade"></div>
  <div class="topbar">
    <span style="left:115px">48 Linden Row, Portvale, NY 10482</span>
    <span style="left:385px">hello@brightdesk.com</span>
    <div class="login">LOGIN</div>
  </div>
  <div class="brand"><i></i>brightdesk</div>
  <nav class="nav">
    <a class="active" href="#" style="left:576px">HOME</a>
    <a href="#" style="left:662px">OUR STORY</a>
    <a href="#" style="left:784px">OUR PEOPLE</a>
    <a href="#" style="left:916px">WHAT WE DO</a>
    <a href="#" style="left:1052px">CONTACT</a>
  </nav>
  <svg class="arrow" style="left:40px" width="30" height="50" viewBox="0 0 30 50"><path d="M26 2 4 25l22 23" fill="none" stroke="#fff" stroke-width="2"/></svg>
  <svg class="arrow" style="left:1120px" width="30" height="50" viewBox="0 0 30 50"><path d="M4 2l22 23L4 48" fill="none" stroke="#fff" stroke-width="2"/></svg>
  <h1>WE FIX YOUR COMPUTER</h1>
  <h2>REMOTE SUPPORT WORLDWIDE</h2>
  <div class="btn btn-white">LEARN MORE</div>
  <div class="btn btn-blue">GET HELP NOW</div>
  <div class="dots"><i></i><i></i><i class="on"></i><i></i><i></i></div>
</header>

<section class="features">
  <div class="fcard" style="left:108px">
    <div class="ico" style="background:#1e8fff"><svg width="36" height="36" viewBox="0 0 24 24"><path d="M21 6.5a5 5 0 0 1-6.6 4.7L6 19.6a1.9 1.9 0 0 1-2.7-2.7l8.4-8.4A5 5 0 0 1 17.5 2l-3 3 .5 3 3 .5z" fill="#fff"/></svg></div>
    <h3>Honest Services</h3>
    <p>Clear prices up front, no hidden fees and no fix, no charge on every call.</p>
  </div>
  <div class="fcard" style="left:360px">
    <div class="ico" style="background:#3f51b5"><svg width="34" height="34" viewBox="0 0 24 24"><circle cx="12" cy="12" r="7" fill="none" stroke="#fff" stroke-width="4" stroke-dasharray="3.2 2.3"/><circle cx="12" cy="12" r="5.5" fill="#fff"/><circle cx="12" cy="12" r="2.3" fill="#3f51b5"/></svg></div>
    <h3>Quick Repair</h3>
    <p>We connect to your computer in minutes and fix it while you watch.</p>
  </div>
  <div class="fcard" style="left:609px">
    <div class="ico" style="background:#673ab7"><svg width="36" height="36" viewBox="0 0 24 24"><path d="M5 12a7 7 0 1 0 2-5" fill="none" stroke="#fff" stroke-width="2.4"/><path d="M3 4v5h5" fill="none" stroke="#fff" stroke-width="2.4"/><path d="M12 8v4l3 2" fill="none" stroke="#fff" stroke-width="2.4"/></svg></div>
    <h3>Help Around the Clock</h3>
    <p>Day or night, in any time zone, a friendly expert is ready to help.</p>
  </div>
  <div class="fcard" style="left:860px">
    <div class="ico" style="background:#f4511e"><svg width="36" height="36" viewBox="0 0 24 24"><path d="M12 20S3 14.5 3 8.8A4.6 4.6 0 0 1 12 7a4.6 4.6 0 0 1 9 1.8C21 14.5 12 20 12 20z" fill="none" stroke="#fff" stroke-width="2.2"/></svg></div>
    <h3>We are passionate</h3>
    <p>Plain words, patient steps and real care for every customer we help.</p>
  </div>
</section>

<section class="band">
  <div class="band-deco" role="img" aria-label="Faint outline of a smartphone with gears"></div>
  <div class="band-rule"></div>
  <div class="band-box"></div>
  <div class="svc" style="left:87px">
    <svg width="36" height="36" viewBox="0 0 24 24"><circle cx="12" cy="12" r="9" fill="none" stroke="#fff" stroke-width="1.8"/><path d="M12 7v5l3 2" fill="none" stroke="#fff" stroke-width="1.8"/></svg>
    <h3>SAME DAY SERVICE</h3>
    <p>Slow computer, pop-ups or a printer that will not work? Most problems are solved the same day.</p>
    <a href="#">LEARN MORE</a>
  </div>
  <div class="svc" style="left:341px">
    <svg width="36" height="36" viewBox="0 0 24 24"><rect x="4" y="5" width="14" height="15" fill="none" stroke="#fff" stroke-width="1.8"/><path d="M10 14l9-9" stroke="#fff" stroke-width="1.8"/></svg>
    <h3>SAFE REMOTE ACCESS</h3>
    <p>Encrypted connection you control. You see every step and can end the session at any time.</p>
    <a href="#">LEARN MORE</a>
  </div>
  <div class="svc" style="left:598px">
    <svg width="36" height="36" viewBox="0 0 24 24"><path d="M3 12h18M6 8h12l2 4-2 4H6l-2-4z" fill="none" stroke="#fff" stroke-width="1.8"/><circle cx="12" cy="5" r="1.5" fill="#fff"/></svg>
    <h3>HOME &amp; BUSINESS</h3>
    <p>Support for home users and small to medium businesses, from one laptop to a whole office.</p>
    <a href="#">LEARN MORE</a>
  </div>
  <div class="svc" style="left:854px">
    <svg width="36" height="36" viewBox="0 0 24 24"><path d="M4 4l16 16M20 4 4 20M3 6l3-3M18 21l3-3" fill="none" stroke="#fff" stroke-width="1.8"/></svg>
    <h3>EXPERT TECHNICIANS</h3>
    <p>Certified, patient technicians who explain each fix in plain words, with no jargon.</p>
    <a href="#">LEARN MORE</a>
  </div>
</section>

<section class="range">
  <h2>WE OFFER A FULL RANGE OF<br>COMPUTER SUPPORT SERVICES</h2>
  <p class="lead">Wherever you are in Europe, the Americas or Asia, our team connects to your computer remotely and fixes it fast.</p>
  <div class="item" style="left:108px;top:248px"><svg width="14" height="18" viewBox="0 0 14 18"><rect x="1" y="1" width="12" height="16" rx="2" fill="none" stroke="#888"/></svg>Slow Computer Speed-Up</div>
  <div class="item" style="left:108px;top:291px"><svg width="14" height="18" viewBox="0 0 14 18"><rect x="1" y="1" width="12" height="16" rx="1" fill="none" stroke="#888"/><path d="M1 13h12" stroke="#888"/></svg>Virus &amp; Malware Removal</div>
  <div class="item" style="left:108px;top:334px"><svg width="14" height="18" viewBox="0 0 14 18"><rect x="1" y="1" width="12" height="16" rx="1" fill="none" stroke="#888"/><path d="M4 6h6M4 9h6" stroke="#888"/></svg>Data Recovery</div>
  <div class="item" style="left:329px;top:248px"><svg width="14" height="18" viewBox="0 0 14 18"><rect x="1" y="1" width="12" height="16" rx="1" fill="none" stroke="#888"/><path d="M4 7h6M4 11h6" stroke="#888"/></svg>Email &amp; Printer Setup</div>
  <div class="item" style="left:329px;top:291px"><svg width="14" height="18" viewBox="0 0 14 18"><rect x="2" y="3" width="10" height="14" fill="none" stroke="#888"/><path d="M5 1h4" stroke="#888" stroke-width="2"/></svg>Software Installs</div>
  <div class="item" style="left:329px;top:334px"><svg width="14" height="18" viewBox="0 0 14 18"><path d="M2 1h7l3 3v13H2z" fill="none" stroke="#888"/><path d="M5 9h4M5 12h4" stroke="#888"/></svg>Wi-Fi &amp; Network Help</div>
  <div class="sq fill">GET HELP NOW</div>
  <div class="sq line">GET A QUOTE</div>
  <div class="device-art" role="img" aria-label="Exploded view of a device showing screen, frame, circuit board and battery layers"></div>
  <svg class="vdots" width="12" height="52" viewBox="0 0 12 52"><circle cx="6" cy="4" r="3" fill="#ccc"/><circle cx="6" cy="26" r="5" fill="none" stroke="#1e8fff"/><circle cx="6" cy="26" r="3" fill="#1e8fff"/><circle cx="6" cy="48" r="3" fill="#ccc"/></svg>
</section>

<section class="plans">
  <h2>Our Support Plans</h2>
  <p class="sub">You, the customer, are the most important part of our business. Get expert remote help at a fair price, for your home or your business, anywhere in the world.</p>
  <div class="plan" style="left:113px"><h4>Bronze</h4><div class="price">26<sup>$</sup></div><div class="at">@ Home</div><p>One remote session to fix your home computer</p><span class="go">GET HELP NOW</span></div>
  <div class="plan" style="left:357px"><h4>Silver</h4><div class="price">36<sup>$</sup></div><div class="at">@ Home</div><p>A month of help for every home computer</p><span class="go">GET HELP NOW</span></div>
  <div class="plan" style="left:602px"><h4>Gold</h4><div class="price">46<sup>$</sup></div><div class="at">@ Business</div><p>Remote help for small business teams</p><span class="go">GET HELP NOW</span></div>
  <div class="plan" style="left:847px"><h4>Platinum</h4><div class="price">56<sup>$</sup></div><div class="at">@ Business</div><p>Priority care for growing office networks</p><span class="go">GET HELP NOW</span></div>
</section>

<section class="regions">
  <h2>We support customers around the globe</h2>
  <p class="sub">Remote computer help in every time zone, for home users and businesses across these regions.</p>
  <div class="rule"></div>
  <div class="rname" style="left:256px">EUROPE</div>
  <div class="rname" style="left:459px">N. AMERICA</div>
  <div class="rname" style="left:667px">S. AMERICA</div>
  <div class="rname" style="left:871px">ASIA</div>
  <div class="rname" style="left:1070px">OCEANIA</div>
</section>

<footer class="footer">
  <div class="fcol" style="left:134px;width:220px">
    <h4>About Brightdesk</h4><div class="rule"></div>
    <p>Brightdesk – remote computer support for homes and small businesses, helping customers across Europe, the Americas and Asia.</p>
    <div class="social"><i></i><i></i><i></i><i></i></div>
  </div>
  <div class="fcol" style="left:392px">
    <h4>Postal Address</h4><div class="rule"></div>
    <ul class="contact">
      <li><svg width="10" height="14" viewBox="0 0 10 14" style="margin-top:5px"><path d="M5 13S1 8 1 5a4 4 0 0 1 8 0c0 3-4 8-4 8z" fill="#ccc"/></svg>72 Harrowgate Lane, Dunmere, TX,<br>4518 USA.</li>
      <li><svg width="12" height="10" viewBox="0 0 12 10" style="margin-top:7px"><rect x=".5" y=".5" width="11" height="9" fill="none" stroke="#ccc"/><path d="M.5.5 6 5l5.5-4.5" fill="none" stroke="#ccc"/></svg>support@brightdesk.com</li>
      <li><svg width="12" height="10" viewBox="0 0 12 10" style="margin-top:7px"><rect x=".5" y=".5" width="11" height="9" fill="none" stroke="#ccc"/><path d="M.5.5 6 5l5.5-4.5" fill="none" stroke="#ccc"/></svg>hello@brightdesk.com</li>
      <li><svg width="12" height="12" viewBox="0 0 12 12" style="margin-top:6px"><path d="M2 1l2 0 1 3-1.5 1a7 7 0 0 0 3.5 3.5L8 7l3 1v2a1 1 0 0 1-1 1A10 10 0 0 1 1 2a1 1 0 0 1 1-1z" fill="#ccc"/></svg>00+1-555-204-7731</li>
      <li><svg width="12" height="12" viewBox="0 0 12 12" style="margin-top:6px"><path d="M2 1l2 0 1 3-1.5 1a7 7 0 0 0 3.5 3.5L8 7l3 1v2a1 1 0 0 1-1 1A10 10 0 0 1 1 2a1 1 0 0 1 1-1z" fill="#ccc"/></svg>00+1-555-204-7732</li>
    </ul>
  </div>
  <div class="fcol" style="left:650px">
    <h4>Problems We Fix</h4><div class="rule"></div>
    <ul><li>Slow Computer Speed-Up</li><li>Virus &amp; Malware Removal</li><li>Email &amp; Printer Setup</li><li>Data Backup &amp; Recovery</li><li>Wi-Fi &amp; Network Help</li></ul>
  </div>
  <div class="fcol" style="left:905px">
    <h4>Information</h4><div class="rule"></div>
    <ul><li>About Brightdesk</li><li>Contact Us</li><li>Blog</li><li>Careers</li><li>Terms &amp; Conditions</li></ul>
  </div>
  <div class="copy">Copyright © 2017 Brightdesk, All rights reserved.</div>
</footer>

</body>
</html>
```